Website for the K7VANT-Lab research laboratory.

We are a research team working on personality disorders. We would like a website that presents the team members (noting that students change frequently), ongoing projects with active recruitments, the latest publications, student resources, and possibly patient resources.

We have already prepared the logo with Plumvetta.

Our research areas:
1- Lifestyle Medicine and BPD
This area focuses on understanding lifestyle habits and their impact on the health of individuals living with Borderline Personality Disorder (BPD). It aims to improve essential components such as sleep, physical activity, and nutrition by identifying and promoting favorable lifestyle habits. The goal is to strengthen emotional regulation and improve overall health by fully integrating the physical dimension into recovery.
2- Interventions Supporting Psychosocial Functioning
Develop the full recovery potential and enhance social and professional integration strategies to support the life journey of patients in all its dimensions. This area focuses on practices and interventions that facilitate a return to an active life and harmonious integration into society.
3- Optimization of Psychotherapeutic Strategies in BPD
Optimize psychotherapeutic approaches for BPD by identifying the most effective methods, adapting them to individual needs, and evaluating their long-term impact. This research area aims to refine and personalize treatments to maximize their therapeutic benefits.
4- Biological Treatments for BPD: Neuromodulation and Pharmacotherapy
Develop and evaluate biological treatments, particularly in neuromodulation and pharmacotherapy, to improve the management of BPD. This area aims to explore scientific advances in these fields to offer complementary and innovative therapeutic options.

Vision
Affiliated with TVOLBAE, our laboratory is dedicated to creating tomorrow's interventions to offer a hopeful future for individuals living with Borderline Personality Disorder. We design and develop innovative solutions that integrate and value each individual, their loved ones, and their community, supporting their personal, social, functional, and physical recovery.

Values

Innovation
Our commitment to innovation guides every step of our research and development. We continually strive to push the boundaries of knowledge and techniques to create new and bold therapeutic solutions tailored to the evolving needs of individuals living with Borderline Personality Disorder.
Hope
We carry the hope of making a real difference in the lives of people living with BPD. This hope drives our work, pushing us to explore therapeutic approaches that offer patients a better and more serene future. By integrating this hope into our research, we are committed to developing interventions that inspire and support the recovery process. Through our research work, we wish to instill and spread hope.
Empathy and Personalization
We believe in a person-centered and inclusive approach where each individual is considered in their uniqueness and with compassion. By actively integrating patients and their experiences into our research, we aim to design solutions that not only meet their specific needs but also value their recovery while respecting their values. We wish to improve the satisfaction of individuals within the care network, promote the integration of their loved ones and their community.

```html
<!DOCTYPE html>
<html lang="en">
<head>
<meta charset="utf-8">
<title>K7VANT-Lab — Personality Disorders Research</title>
<link href="https://fonts.googleapis.com/css2?family=Nunito+Sans:wght@400;600;700;800&family=Nunito:wght@400;600;700&display=swap" rel="stylesheet">
<style>
:root{
  --blue:#0a84d0;
  --blue-text:#1a87d6;
  --green:#3cb54a;
  --ink:#1b1b1b;
  --body:#333;
  --navy:#0b2236;
  --mist:#eef6fb;
  --card-line:#eceff2;
}
*{box-sizing:border-box;margin:0;padding:0}
html,body{width:1200px;height:4435px;overflow:hidden}
body{font-family:"Nunito",sans-serif;color:var(--body);background:#fff;position:relative}
h1,h2,h3,h4{font-family:"Nunito Sans",sans-serif;color:var(--ink)}
.abs{position:absolute}
.btn{display:inline-flex;align-items:center;justify-content:center;background:var(--green);color:#fff;font-size:19px;font-family:"Nunito",sans-serif;text-decoration:none;box-shadow:0 2px 4px rgba(0,0,0,.15)}
.brand{display:flex;align-items:center;gap:10px;font-family:"Nunito Sans",sans-serif;font-weight:800;font-size:36px;color:var(--blue-text)}
.brand-dot{width:38px;height:38px;border-radius:50%;background:var(--green)}

/* header */
.site-header{position:absolute;left:0;top:0;width:1200px;height:115px;background:#fff;box-shadow:0 1px 3px rgba(0,0,0,.06)}
.site-header .brand{position:absolute;left:83px;top:38px}
.main-nav{position:absolute;right:83px;top:48px;display:flex;gap:25px;font-size:13px;font-family:"Nunito Sans",sans-serif;color:#222;text-transform:uppercase}
.main-nav .active{color:var(--green)}

/* hero */
.hero{position:absolute;left:0;top:115px;width:1200px;height:560px;background:linear-gradient(160deg,#e6f3fb 0%,#f4faf6 60%,#fff 100%)}
.hero h1{position:absolute;left:83px;top:115px;font-size:41px;line-height:43px;font-weight:700}
.hero h1 .b{color:var(--blue-text)} .hero h1 .g{color:var(--green)}
.hero p{position:absolute;left:83px;top:258px;width:460px;font-size:17px;line-height:25px}
.hero .btn{position:absolute;left:83px;top:402px;width:180px;height:63px}
.photo-circle{position:absolute;border-radius:50%}
.hero .photo-circle{left:668px;top:65px;width:448px;height:448px;background:radial-gradient(circle at 45% 40%,#9fd0f0,#2f86c8 70%,#1a5e9a)}

/* vision */
.vision .photo-circle{left:83px;top:737px;width:411px;height:411px;background:radial-gradient(circle at 50% 40%,#e8c1a2,#5b4a3c 55%,#1f4a3c)}
.vision h2{position:absolute;left:635px;top:776px;font-size:38px;font-weight:700}
.vision p{position:absolute;left:635px;top:833px;width:480px;font-size:17px;line-height:25px}
.vision .btn{position:absolute;left:635px;top:1026px;width:180px;height:64px}

/* research */
.research{position:absolute;left:0;top:1228px;width:1200px;height:642px;background:var(--blue);overflow:hidden}
.research h2{position:absolute;left:0;width:1200px;top:60px;text-align:center;color:#fff;font-size:38px;font-weight:700}
.area-card{position:absolute;top:136px;height:382px;background:#fff;border-radius:12px}
.area-card .pic{position:absolute;left:25px;top:24px;width:395px;height:334px;border-radius:8px}
.area-card h3{position:absolute;left:445px;top:80px;font-size:29px;font-weight:600}
.area-card p{position:absolute;left:445px;top:125px;width:430px;font-size:15.5px;line-height:22.5px}
.dots{position:absolute;left:0;width:1200px;display:flex;justify-content:center;gap:7px}
.dots span{width:12px;height:12px;border-radius:50%;background:rgba(255,255,255,.5)}
.dots span.on{background:#fff}
.dots.dark span{background:#cfe3f2}
.dots.dark span.on{background:var(--blue)}

/* values */
.values h2{position:absolute;left:0;width:1200px;top:1938px;text-align:center;font-size:38px;font-weight:700}
.value-card{position:absolute;top:2003px;width:325px;height:344px;background:#fff;border-radius:10px;box-shadow:0 0 12px rgba(0,0,0,.07);text-align:center;padding:30px 18px 0}
.value-card svg{width:60px;height:60px}
.value-card h3{font-size:25px;line-height:27px;font-weight:700;margin:10px 0 10px}
.value-card p{font-size:15.5px;line-height:22px}
.value-card a{color:var(--green);text-decoration:none}

/* team */
.team{position:absolute;left:0;top:2428px;width:1200px;height:642px;background:var(--mist)}
.team h2{position:absolute;left:0;width:1200px;top:70px;text-align:center;font-size:38px;font-weight:700}
.team .intro{position:absolute;left:0;width:1200px;top:124px;text-align:center;font-size:16px;line-height:22px}
.team .note{position:absolute;left:0;width:1200px;top:178px;text-align:center;font-size:16px;line-height:22px;font-style:italic;font-weight:700;color:#222}
.member{position:absolute;top:250px;width:260px;text-align:center}
.member .avatar{width:190px;height:190px;border-radius:50%;margin:0 auto 18px}
.member h4{font-size:18px;font-weight:600}
.member p{font-size:14px;line-height:18px;color:#444}

/* publications */
.pubs h2{position:absolute;left:0;width:1200px;top:3138px;text-align:center;font-size:38px;font-weight:700}
.pub-card{position:absolute;top:3213px;width:310px;height:460px;background:#fff;border-radius:10px;box-shadow:0 0 12px rgba(0,0,0,.07);padding:14px 14px 0}
.pub-card .pic{height:216px;border-radius:8px}
.pub-card h3{font-size:18px;line-height:21px;font-weight:700;margin:16px 0 8px}
.pub-card p{font-size:14px;line-height:18px;color:#333}
.pub-card .more{display:inline-block;margin-top:10px;border:1px solid var(--blue-text);color:var(--blue-text);font-size:14px;padding:6px 15px;border-radius:3px;text-decoration:none}
.arrow{position:absolute;top:3425px;width:36px;height:36px;border-radius:50%;border:1.5px solid var(--blue-text);display:flex;align-items:center;justify-content:center}
.pubs .btn{position:absolute;left:477px;top:3704px;width:246px;height:64px}

/* footer */
.site-footer{position:absolute;left:0;top:3987px;width:1200px;height:448px;background:var(--navy)}
.cta{position:absolute;left:83px;top:3849px;width:1033px;height:275px;border-radius:138px;background:linear-gradient(90deg,#1090d6 0%,#1aa39a 50%,#3cb54a 100%);text-align:center;color:#fff}
.cta h2{color:#fff;font-size:40px;font-weight:700;margin-top:58px}
.cta p{font-size:16px;line-height:22px;margin-top:6px}
.cta .actions{display:flex;justify-content:center;gap:24px;margin-top:20px}
.cta .actions a{border:1.5px solid #fff;color:#fff;font-size:18px;width:202px;height:44px;display:flex;align-items:center;justify-content:center;text-decoration:none}
.site-footer .brand{position:absolute;left:83px;top:200px}
.foot-col{position:absolute;top:198px;font-size:13px;line-height:21px;color:#fff}
.foot-col h4{color:var(--blue-text);font-size:16px;font-weight:600;margin-bottom:6px;letter-spacing:.3px}
.foot-col li{list-style:none;display:flex;gap:8px;align-items:flex-start}
.foot-col svg{flex:none;margin-top:5px}
.socials{display:flex;gap:6px}
.socials span{width:13px;height:13px;border-radius:50%;background:var(--green)}
.partner-badge{position:absolute;left:919px;top:197px;width:197px;height:121px;background:#fff;border-radius:6px}
.partner-badge span{position:absolute;left:20px;top:30px;width:60px;height:60px;border-radius:50%;background:#f1c232}
.partner-badge i{position:absolute;left:95px;top:48px;width:80px;height:24px;background:#d6e9f7;border-radius:3px}
.site-footer hr{position:absolute;left:83px;top:386px;width:1033px;border:0;border-top:1px solid rgba(255,255,255,.12)}
.copyright{position:absolute;left:0;width:1200px;top:417px;text-align:center;font-size:12px;color:#aab4be}
</style>
</head>
<body>

<header class="site-header">
  <div class="brand"><span class="brand-dot"></span>K7VANT</div>
  <nav class="main-nav">
    <span class="active">Home</span><span>About Us ▾</span><span>Research Areas</span><span>Get Involved ▾</span><span>Resources ▾</span><span>Publications</span><span>Contact Us</span>
  </nav>
</header>

<section class="hero">
  <h1>Advancing Research in<br><span class="b">Personality Disorders</span><br>for a <span class="g">Healthier Future</span></h1>
  <p>At K7VANT-Lab, we pioneer cutting-edge research to improve the lives of individuals with Borderline Personality Disorder. Through innovation, compassion, and scientific excellence, we are shaping the future of treatment and recovery.</p>
  <a class="btn" href="#">Get Involved</a>
  <div class="photo-circle" role="img" aria-label="Researcher in lab coat examining a test tube"></div>
</section>

<section class="vision">
  <div class="photo-circle" role="img" aria-label="Smiling woman in a green blouse"></div>
  <h2>Our Vision</h2>
  <p>Affiliated with TVOLBAE, our laboratory is dedicated to creating tomorrow's interventions to offer a hopeful future for individuals living with Borderline Personality Disorder. We design and develop innovative solutions that integrate and value each individual, their loved ones, and their community, supporting their personal, social, functional, and physical recovery.</p>
  <a class="btn" href="#">Get Involved</a>
</section>

<section class="research">
  <h2>Our Research Areas</h2>
  <article class="area-card" style="left:83px;width:902px">
    <div class="pic" role="img" aria-label="Man eating a healthy salad bowl on a sofa" style="background:linear-gradient(135deg,#c9d6b4,#6f8a5a 60%,#3f5a3a)"></div>
    <h3>Lifestyle Medicine and BPD</h3>
    <p>This area focuses on understanding lifestyle habits and their impact on the health of individuals living with Borderline Personality Disorder (BPD). It aims to improve essential components such as sleep, physical activity, and nutrition by identifying and promoting favorable lifestyle habits. The goal is to strengthen emotional regulation and improve overall health by fully integrating the physical dimension into recovery.</p>
  </article>
  <article class="area-card" style="left:1026px;width:300px">
    <div class="pic" role="img" aria-label="Women talking over coffee at a café table" style="left:25px;width:260px;background:linear-gradient(135deg,#e9e2d4,#b79a76 60%,#6c5a48)"></div>
  </article>
  <div class="dots" style="top:556px"><span class="on"></span><span></span><span></span><span></span></div>
</section>

<section class="values">
  <h2>Our Values</h2>
  <article class="value-card" style="left:88px">
    <svg viewBox="0 0 60 60" fill="none" stroke="#2aa86a" stroke-width="2.5" stroke-linecap="round"><circle cx="30" cy="25" r="13"/><path d="M24 38v8h12v-8M26 50h8M30 5v4M12 25H8M52 25h-4M17 12l-3-3M43 12l3-3"/><circle cx="30" cy="25" r="5"/></svg>
    <h3>Innovation</h3>
    <p>Our commitment to innovation guides every step of our research and development. We continually strive to push the boundaries of knowledge and techniques to create new and bold therapeutic solutions tailored to the evolving needs of individuals living with Borderline Personality Disorder.</p>
  </article>
  <article class="value-card" style="left:441px">
    <svg viewBox="0 0 60 60" fill="none" stroke-width="2.5" stroke-linecap="round"><path d="M14 44a16 16 0 0 1 32 0" stroke="#1a87d6"/><path d="M4 48h52" stroke="#2aa86a"/><path d="M30 12v8M12 20l5 5M48 20l-5 5M4 34h6M50 34h6" stroke="#2aa86a"/></svg>
    <h3>Hope</h3>
    <p>We carry the hope of making a real difference in the lives of people living with BPD. This hope drives our work, pushing us to explore therapeutic approaches that offer patients a better and more serene future. By integrating this hope into our research, we are committed to developing ...<a href="#">Read more</a></p>
  </article>
  <article class="value-card" style="left:792px">
    <svg viewBox="0 0 60 60" fill="none" stroke-width="2.5" stroke-linejoin="round"><path d="M30 26c-6-5-10-8-10-12a5 5 0 0 1 10-1 5 5 0 0 1 10 1c0 4-4 7-10 12z" stroke="#2aa86a"/><path d="M8 20l6 18 10 8v10M52 20l-6 18-10 8v10" stroke="#1a87d6"/></svg>
    <h3>Empathy and<br>Personalization</h3>
    <p>We believe in a person-centered and inclusive approach where each individual is considered in their uniqueness and with compassion. By actively integrating patients and their experiences into our research, we aim to design solutions that ...<a href="#">Read more</a></p>
  </article>
</section>

<section class="team">
  <h2>Our Team</h2>
  <p class="intro">We are a dedicated research team committed to advancing knowledge and developing<br>innovative interventions for individuals living with Borderline Personality Disorder (BPD).</p>
  <p class="note">Note: As research is a dynamic field, student team members change frequently.<br>We appreciate the contributions of all past and present students to our ongoing projects.</p>
  <div class="member" style="left:85px"><div class="avatar" role="img" aria-label="Portrait of Dr. Elias Marrow" style="background:#f28a1c"></div><h4>Dr. Elias Marrow</h4><p>Clinical Psychiatrist &amp;<br>Research Lead</p></div>
  <div class="member" style="left:342px"><div class="avatar" role="img" aria-label="Portrait of Dr. Tobin Vasquel" style="background:#b7c820"></div><h4>Dr. Tobin Vasquel</h4><p>Lead Researcher,<br>Psychosocial Interventions</p></div>
  <div class="member" style="left:598px"><div class="avatar" role="img" aria-label="Portrait of Dr. Ana Sorell" style="background:#4cc04a"></div><h4>Dr. Ana Sorell</h4><p>Lifestyle Medicine &amp;<br>Mental Health Researcher</p></div>
  <div class="member" style="left:855px"><div class="avatar" role="img" aria-label="Portrait of Noah Brevik" style="background:#1fb0a6"></div><h4>Noah Brevik</h4><p>Student Researcher</p></div>
  <div class="dots dark" style="top:550px"><span class="on"></span><span></span><span></span><span></span></div>
</section>

<section class="pubs">
  <h2>Latest Publications</h2>
  <div class="arrow" style="left:42px"><svg width="14" height="14" viewBox="0 0 14 14" fill="none" stroke="#1a87d6" stroke-width="1.6"><path d="M8 3L4 7l4 4M4 7h7"/></svg></div>
  <article class="pub-card" style="left:95px">
    <div class="pic" role="img" aria-label="Man sleeping peacefully on a white pillow" style="background:linear-gradient(135deg,#f2f2f0,#c9c4bc 60%,#8a7a6a)"></div>
    <h3>Understanding the Role of Sleep in Emotional Regulation for Individuals with BPD</h3>
    <p>Explores the impact of sleep quality on emotional stability in individuals with BPD and highlights lifestyle-based interventions for improving sleep patterns.</p>
    <a class="more" href="#">Learn More</a>
  </article>
  <article class="pub-card" style="left:444px">
    <div class="pic" role="img" aria-label="Friends laughing together at a café table" style="background:linear-gradient(135deg,#efe6d4,#c99a5a 55%,#6a4a30)"></div>
    <h3>Advancing Psychosocial Interventions: Strategies for Social and Professional Integration</h3>
    <p>Discusses evidence-based approaches to enhancing social and professional reintegration for individuals recovering from BPD.</p>
    <a class="more" href="#">Learn More</a>
  </article>
  <article class="pub-card" style="left:795px">
    <div class="pic" role="img" aria-label="Doctor holding a glowing model of the brain" style="background:linear-gradient(135deg,#d8e8f4,#8fb4d6 55%,#e8a27a)"></div>
    <h3>Neuromodulation as a Promising Treatment for BPD: Current Evidence and Future Directions</h3>
    <p>Examines the latest advancements in neuromodulation techniques and their potential role in managing BPD symptoms.</p>
    <a class="more" href="#">Learn More</a>
  </article>
  <div class="arrow" style="left:1120px"><svg width="14" height="14" viewBox="0 0 14 14" fill="none" stroke="#1a87d6" stroke-width="1.6"><path d="M6 3l4 4-4 4M10 7H3"/></svg></div>
  <a class="btn" href="#">See All Publications</a>
</section>

<footer class="site-footer">
  <div class="brand"><span class="brand-dot"></span>K7VANT</div>
  <div class="foot-col" style="left:337px">
    <h4>QUICK LINKS</h4>
    <ul><li>Home</li><li>About Us</li><li>Research Areas</li><li>Get Involved</li><li>Resources</li><li>Publications</li><li>Contact Us</li></ul>
  </div>
  <div class="foot-col" style="left:517px">
    <h4>CONTACT US</h4>
    <ul>
      <li><svg width="11" height="9" viewBox="0 0 11 9"><rect x=".5" y=".5" width="10" height="8" fill="none" stroke="#3cb54a"/><path d="M1 1l4.5 4L10 1" fill="none" stroke="#3cb54a"/></svg>info@k7vant.org</li>
      <li style="margin-top:6px"><svg width="10" height="10" viewBox="0 0 10 10"><path d="M2 1l2 2-1 1.5a6 6 0 0 0 2.5 2.5L7 6l2 2-1.5 1.5C4 9 1 6 .5 2.5z" fill="#3cb54a"/></svg>+1 (555) 014-2290</li>
      <li style="margin-top:6px"><svg width="9" height="11" viewBox="0 0 9 11"><path d="M4.5 11S0 6 0 4a4.5 4.5 0 0 1 9 0c0 2-4.5 7-4.5 7z" fill="#3cb54a"/></svg>2480, rue Valmorin,<br>Montréal (Québec)<br>H0H 0H0</li>
    </ul>
  </div>
  <div class="foot-col" style="left:739px">
    <h4>FOLLOW US</h4>
    <div class="socials"><span></span><span></span></div>
  </div>
  <div class="partner-badge" role="img" aria-label="Affiliated research centre badge"><span></span><i></i></div>
  <hr>
  <p class="copyright">© 2025 K7VANT Research Lab. All Rights Reserved.</p>
</footer>

<section class="cta">
  <h2>Get Involved</h2>
  <p>Your support—whether through funding, collaboration, or<br>participation—helps us push boundaries and improve lives.</p>
  <div class="actions"><a href="#">Support Our Work</a><a href="#">Join Our Team</a></div>
</section>

</body>
</html>
```